Business Card for Auto Dealership - Clean, sharp and professional

Please use the maroon logo with the grey background. Need a sharp, clean and professional business card for an Auto Dealer. In the files provides there is three different logos. I have not decided which one to go with yet. Right now I am favoring the grey/silver background. I would like my contact info on there and the website as well. I feel like less is more and want something simple, clean and sharp. Thank you in advance for your tie and effort! I also need email signature, letterhead, etc after this

Target Market(s)

Car buyers

Industry/Entity Type

Automotive

Contact Information for Business Card

Dean
555-417-2386
www.BrinwoodAutoHub.example
Dean@BrinwoodAutoHub.example

Font styles to use
Serif
Sans Serif

Requirements
Must have
• Please use the maroon logo with the grey background. Business Card Details and logo from files. Please stick to the logo colors

```html
<!DOCTYPE html>
<html lang="en">
<head>
<meta charset="utf-8">
<title>Brinwood Auto Hub – Business Card</title>
<link href="https://fonts.googleapis.com/css2?family=Exo+2:wght@400;700;800&display=swap" rel="stylesheet">
<style>
  :root {
    --maroon: #5e1618;
    --maroon-faint: rgba(94, 22, 24, 0.07);
    --silver-light: #fbfbfb;
    --silver-mid: #e6e6e6;
    --silver-dark: #cfcfcf;
    --backdrop: #1e1e1e;
  }
  * { box-sizing: border-box; margin: 0; padding: 0; }
  html, body {
    width: 1200px; height: 800px; overflow: hidden;
    background: var(--backdrop);
    font-family: "Exo 2", Arial, sans-serif;
  }
  .stage {
    width: 1200px; height: 800px;
    display: flex; align-items: center; justify-content: center; gap: 60px;
  }
  .card {
    position: relative; width: 525px; height: 300px; overflow: hidden;
    background: linear-gradient(135deg, var(--silver-light) 0%, var(--silver-mid) 55%, var(--silver-dark) 100%);
    box-shadow: 0 14px 30px rgba(0,0,0,0.55);
  }
  /* Front side */
  .front .faint-ring {
    position: absolute; left: 170px; top: 40px; width: 220px; height: 220px;
    border-radius: 50%; border: 22px solid var(--maroon-faint);
  }
  .front .brand {
    position: absolute; left: 0; right: 0; top: 50%; transform: translateY(-50%);
    display: flex; align-items: center; justify-content: center; gap: 16px;
  }
  .brand-dot {
    width: 44px; height: 44px; border-radius: 50%; background: var(--maroon);
  }
  .wordmark { color: var(--maroon); font-weight: 800; text-transform: uppercase; line-height: 1; }
  .wordmark .primary { display: block; font-size: 44px; letter-spacing: 1px; }
  .wordmark .secondary { display: block; font-size: 14px; letter-spacing: 7px; font-weight: 800; margin-top: 2px; text-align: right; }

  /* Back side */
  .back .header-band {
    position: absolute; left: 0; top: 0; width: 100%; height: 92px;
    background: linear-gradient(180deg, #ffffff, #ececec);
    border-bottom: 1px solid #d4d4d4;
  }
  .back .wordmark { position: absolute; left: 34px; top: 22px; }
  .back .wordmark .primary { font-size: 34px; }
  .back .wordmark .secondary { font-size: 11px; letter-spacing: 6px; }
  .contact {
    position: absolute; left: 34px; top: 118px; color: var(--maroon);
  }
  .contact .person { font-size: 28px; font-weight: 800; text-transform: uppercase; letter-spacing: 1px; }
  .contact .phone { display: flex; align-items: center; gap: 6px; font-size: 24px; margin-top: 2px; }
  .contact .phone svg { width: 16px; height: 16px; }
  .contact .line { font-size: 13px; margin-top: 5px; }
  .back .seal {
    position: absolute; right: -20px; top: 70px; width: 250px; height: 250px;
    border-radius: 50%; background: #ffffff;
    border: 26px solid var(--maroon); box-shadow: 0 0 0 6px #ffffff, 0 0 0 8px var(--maroon);
  }
</style>
</head>
<body>
<main class="stage">
  <section class="card front" aria-label="Business card front">
    <div class="faint-ring"></div>
    <div class="brand">
      <span class="brand-dot"></span>
      <span class="wordmark">
        <span class="primary">Brinwood</span>
        <span class="secondary">Auto Hub</span>
      </span>
    </div>
  </section>

  <section class="card back" aria-label="Business card back">
    <div class="header-band"></div>
    <span class="wordmark">
      <span class="primary">Brinwood</span>
      <span class="secondary">Auto Hub</span>
    </span>
    <div class="contact">
      <p class="person">Dean</p>
      <p class="phone">
        <svg viewBox="0 0 24 24" aria-hidden="true"><path fill="#5e1618" d="M6.6 10.8a15 15 0 0 0 6.6 6.6l2.2-2.2a1 1 0 0 1 1-.25 11.4 11.4 0 0 0 3.6.57 1 1 0 0 1 1 1V20a1 1 0 0 1-1 1A17 17 0 0 1 3 4a1 1 0 0 1 1-1h3.5a1 1 0 0 1 1 1c0 1.25.2 2.45.57 3.57a1 1 0 0 1-.25 1z"/></svg>
        555-417-2386
      </p>
      <p class="line">Dean@BrinwoodAutoHub.example</p>
      <p class="line">www.BrinwoodAutoHub.example</p>
    </div>
    <div class="seal"></div>
  </section>
</main>
</body>
</html>
```